An international recruitment business looking to attract new engineering and construction clients i

BK Worldwide is an international recruitment company with a wealth of experienced engineers, quantity surveyors and construction specialists appropriate to fill roles in the vastly growing Middle East. We need a new, attractive brochure design to send to new clients/companies so they will be interested in our recruitment company and our candidates. We have provided our company logo which we would like to feature, and we would like the theme to match this to some extent. We have also attached our current brochure which should be used for the general content and information. PLEASE NOTE: Ignore the appraisals on the penultimate page - I will provide new ones in a separate document. (Use the one with 5 appraisals, not 3!)
The final design should be modern and attractive and should feature some images of the Middle East including some impressive buildings and new railways (similar to our current ones).
Please also link our website
and use it for inspiration: http://www.bk-worldwide.co.uk
Updates
We would like the brochure to be A5 and landscape - although it will only be emailed to clients and not printed.
There is no limit on number of pages.
There seems to be a problem opening the appraisals document I attached.
The content of this document is:
BK Worldwide Appraisals
"I had the pleasure of working with BK Worldwide as a client and found them to be a great recruiter with in-depth rail knowledge, I had great results from them time after time. I found the team very trustworthy, professional and fun to work with. I would highly recommend BK Worldwide and will continue to use the company for all my future recruitment needs"
Tarek Olivastro, Dunemark Transit Company
“When looking to advance my career, I enquired with BK Worldwide about a senior position in the Middle East. I dealt specifically with Colin who I found very helpful. He informed me of all the job requirements, the background of the role, responsibilities and package. Colin was extremely diligent in moving the process forward and throughout kept in contact and abreast of the situation. In all it proved a great success and I am now happily placed in my new role. Even though Colin performed beyond the normal boundaries of his role he even now keeps in contact to make sure everything is ok and all parties happy and satisfied with the outcome. I wholeheartedly endorse Colin and BK Worldwide and will use them when I am next supplementing my team.”
Miles Thornbury, Head of Quantity Surveying, Vellum Gulf Design Partners (VGDP), Kuwait
BK Worldwide is a recruitment company that has an insatiable appetite for understanding the jobs, for which they recruit, and not only the jobs, but they also establish excellent rapport with the clients and candidates. They are always there when I need to fill positions in my organization quickly. They listen to what I need and always supply me with the resumes that I could review right away to start hiring who I needed - saving me time and effort. They are always able to supply me with the exact person that I need for the open position."
Nadia Faris, HR Consultant, Dunemark Transit
Target Market(s)
Professional clients in the Middle East
Industry/Entity Type
Construction
Colors
Designer to choose colors to be used in the design.
Look and feel

```html
<!DOCTYPE html>
<html lang="en">
<head>
<meta charset="utf-8">
<title>BK Worldwide – A Service Like No Other</title>
<link href="https://fonts.googleapis.com/css2?family=Open+Sans:wght@400;500;600&display=swap" rel="stylesheet">
<style>
  :root {
    --bg: #35383c;
    --teal: #3fb1c0;
    --white: #ffffff;
    --text: #ffffff;
  }
  html, body {
    margin: 0;
    padding: 0;
    overflow: hidden;
    background: var(--bg);
  }
  .page {
    position: relative;
    width: 1200px;
    height: 848px;
    background: var(--bg);
    font-family: "Open Sans", Arial, sans-serif;
    overflow: hidden;
  }
  .page-title {
    position: absolute;
    top: 118px;
    left: 0;
    width: 100%;
    margin: 0;
    text-align: center;
    color: var(--teal);
    font-size: 30px;
    font-weight: 500;
    letter-spacing: 0;
    text-transform: uppercase;
  }
  .feature-photo {
    position: absolute;
    top: 205px;
    width: 196px;
    height: 196px;
    border-radius: 50%;
    border: 8px solid var(--white);
    box-shadow: 0 0 0 11px var(--teal);
  }
  .photo-support  { left: 66px;  background: radial-gradient(circle at 45% 40%, #e8d8cc 0%, #c9b3a3 40%, #eef1f3 75%); }
  .photo-towers   { left: 348px; background: linear-gradient(135deg, #f2f2f2 0%, #8c8f92 45%, #3c3f42 55%, #d9dadb 100%); }
  .photo-network  { left: 634px; background: radial-gradient(circle at 55% 45%, #f5f8fa 0%, #dbe6ee 60%, #b8ccda 100%); }
  .photo-meeting  { left: 915px; background: linear-gradient(160deg, #7a98b3 0%, #3f5e7d 50%, #2a3f57 100%); }

  .feature-text {
    position: absolute;
    top: 452px;
    margin: 0;
    color: var(--text);
    font-size: 17.5px;
    line-height: 26px;
    text-align: center;
    white-space: nowrap;
    transform: translateX(-50%);
  }
  .text-consultants { left: 200px; }
  .text-quality     { left: 463px; }
  .text-one-stop    { left: 742px; }
  .text-next-step   { left: 1024px; }

  .column-divider {
    position: absolute;
    top: 453px;
    width: 4px;
    height: 291px;
    background: var(--teal);
  }
  .divider-one   { left: 320px; }
  .divider-two   { left: 600px; }
  .divider-three { left: 881px; }
</style>
</head>
<body>
  <main class="page">
    <h1 class="page-title">A Service Like No Other...</h1>

    <div class="feature-photo photo-support" role="img" aria-label="Photo of a smiling call-centre consultant wearing a headset"></div>
    <div class="feature-photo photo-towers" role="img" aria-label="Photo looking up at glass skyscrapers"></div>
    <div class="feature-photo photo-network" role="img" aria-label="Photo of a hand drawing a network of connected people icons"></div>
    <div class="feature-photo photo-meeting" role="img" aria-label="Photo of a business meeting table with laptops and documents"></div>

    <p class="feature-text text-consultants">You will benefit from the<br>knowledge and experience<br>of our trained consultants;<br>with an exceptional<br>understanding of the<br>industry sectors as well as<br>the locations and cultures<br>across the Middle East<br>regions.</p>

    <span class="column-divider divider-one"></span>

    <p class="feature-text text-quality">We aim to provide “Quality<br>not Quantity” which is the<br>thought process used prior<br>to submitting any candidate<br>to our<br>clients.</p>

    <span class="column-divider divider-two"></span>

    <p class="feature-text text-one-stop">Our aim is to give our<br>clients a full, one stop<br>recruitment service. Using in<br>–depth knowledge of the<br>market, we have the<br>ability to target hard to<br>source professionals for<br>specific positions within your<br>organisation.</p>

    <span class="column-divider divider-three"></span>

    <p class="feature-text text-next-step">BK Worldwide is the next<br>step for your company in<br>ensuring progression &amp;<br>development with the<br>acquisition of highly<br>skilled professionals.</p>
  </main>
</body>
</html>
```